Wordpress Web page design

We are looking for a new bright client landing page website. the site must be bright, welcoming, professional and mention the services that we offer. Check out www.brightmarkchecks.co.uk for a list of our services. Please note that we have changed our logo from the main site and will be looking to revamp the main site at a later date. This site needs to be totally different to our existing site, we do not want a black background and lots of text. The website needs to have functionality built in to allow clients to log into our site and be taken to their own custom page. Clients should not be able to access other clients' pages. Users that are not logged in should not be able to see any client pages. Provide clients with an easy way to log in. Automated email of username and password would be beneficial. This is for us to be able to place documents, certificates or image downloads, special links, or whatever else we want on to the client page, where we can give them access to files/links. We are not giving them the ability to post on a blog or anything like that. New logo is added and should appear on site. Whatever theme we go for is what our main page will need to be updated to also, so some seo would help
Updates

Project Deadline Extended
Reason: Some good designs submitted but none that really have the style and clean lines that we are looking for. We've extended the deadline to allow for some fresh and new designs to be submitted as we are aware that these things take time to get right

Target Market(s)

busineses that have already used our services and where we can direct them to download test results etc.

Industry/Entity Type

Seo

Requirements
Must have
• must have client log in functionality. Must be easy for us to upload files and images etc. to any specific client page, Automated username, password and email generation would be beneficial. Sites like http://www.tolvane-imaging.com/, or in our industry http://www.ruvenaudit.co.uk/ have the functionality that we need. .
Nice to have
• list of sites we quite like
http://www.corlate-amber.com/ http://www.ruvenaudit.co.uk/
http://www.venquistmedia.com/

Should not have
• dark background, cluttered appearance

```html
<!DOCTYPE html>
<html lang="en">
<head>
<meta charset="utf-8">
<title>Brightmark – Electrical and Safety Testing</title>
<link href="https://fonts.googleapis.com/css2?family=PT+Sans+Narrow:wght@400;700&family=Arimo:wght@400;700&family=Yanone+Kaffeesatz:wght@400&display=swap" rel="stylesheet">
<style>
:root{
  --navy:#0d3f78;
  --blue:#0a58b5;
  --blue-dark:#063a86;
  --teal:#1d95a6;
  --teal-light:#5fc9d4;
  --sky:#4fb4e6;
  --page:#f4f4f4;
  --text:#555;
  --heading:#0f3d73;
  --white:#fff;
  --cyan:#3fd0f0;
}
*{box-sizing:border-box;margin:0;padding:0}
html,body{width:701px;height:1200px;overflow:hidden}
body{background:var(--page);font-family:"Arimo",Arial,sans-serif;color:var(--text);position:relative}
.abs{position:absolute}

/* header */
.site-header{left:0;top:0;width:701px;height:79px;background:linear-gradient(#f2f2f2,#e6e6e6)}
.brand{left:35px;top:22px;display:flex;align-items:center;gap:8px}
.brand-mark{width:30px;height:30px;border-radius:50%;background:var(--blue)}
.brand-name{font-family:"Arimo",sans-serif;font-weight:700;font-size:26px;color:var(--blue-dark)}
.call{right:36px;top:28px;text-align:left;color:var(--navy)}
.call small{display:block;font-size:9.5px;letter-spacing:.2px}
.call strong{display:block;font-weight:400;font-size:16px;color:#444}

/* nav */
.main-nav{left:0;top:79px;width:701px;height:28px;background:linear-gradient(#1a6fd0,#0a4fa8);border-bottom:1px solid #0a3c86;display:flex;justify-content:space-between;align-items:center;padding:0 24px 0 33px}
.main-nav a{color:var(--white);font-size:9.5px;text-decoration:none}

/* hero */
.hero{left:0;top:107px;width:701px;height:184px;background:radial-gradient(ellipse at 45% 40%,var(--teal-light),var(--teal) 55%,#10707f)}
.hero h1{left:20px;top:17px;width:320px;text-align:center;font-family:"Yanone Kaffeesatz",sans-serif;font-weight:400;font-size:34px;line-height:39px;color:var(--white);text-shadow:1px 2px 3px rgba(0,0,0,.45)}
.hero-art{left:424px;top:2px;width:244px;height:180px;background:linear-gradient(135deg,#e9ecef,#b9c4cc 45%,#c8413a 70%,#2f8a4f);opacity:.85}
.hero-rule{left:0;top:294px;width:701px;height:2px;background:#d8d8d8}

/* services */
.service{width:220px;height:70px}
.service .thumb{left:0;top:0;width:70px;height:66px;border:1px solid #d6d6d6;border-radius:5px}
.service h3{left:80px;top:0;font-family:"PT Sans Narrow",sans-serif;font-weight:400;font-size:13px;color:var(--heading)}
.service p{left:80px;top:17px;width:130px;font-size:8.5px;line-height:10.6px;color:#777}
.service .more{left:80px;top:56px;font-size:7px;color:var(--blue-dark)}

/* sidebar */
.login{left:480px;top:311px;width:187px;height:184px;background:linear-gradient(#0d3c76,#0f5aa8 55%,#1c7cc8);border:1px solid #3f88d0}
.login h2{left:0;top:12px;width:100%;text-align:center;font-size:13.5px;line-height:15px;color:var(--white);font-weight:700}
.field{left:11px;width:165px;height:19px;background:var(--white);border:1px solid #9bb;font-size:7.5px;color:#555;padding:5px 6px}
.btn-login{left:11px;top:113px;width:42px;height:19px;background:linear-gradient(#4fb4ec,#1f7fcc);border:1px solid #0a4d91;color:#0b2d5a;font-size:10px;text-align:center;line-height:17px}
.forgot{left:59px;top:118px;font-size:7.5px;color:var(--white)}
.reg-q{left:12px;top:146px;font-size:9.5px;font-weight:700;color:var(--white)}
.reg{left:12px;top:159px;font-size:13px;font-weight:700;color:var(--white)}
.reg span{color:var(--cyan)}
.follow{left:482px;top:520px;width:186px;height:56px;display:flex;align-items:center;gap:8px}
.follow-text{font-family:"Arimo",sans-serif;font-size:19px;line-height:20px;color:#3ab1e4}
.follow-dot{width:36px;height:36px;border-radius:50%;background:#4aa9df;flex:none}
.news{left:480px;top:582px;width:187px;height:132px;background:var(--navy);border:1px solid #2c76c4}
.news h2{left:0;top:12px;width:100%;text-align:center;font-size:13.5px;color:var(--white);font-weight:700}
.news .divider{left:0;top:36px;width:100%;height:1px;background:#3567a0}
.news h4{left:9px;top:44px;font-size:8.5px;color:var(--cyan);font-weight:700}
.news p{left:9px;top:58px;width:170px;font-size:7.2px;line-height:10px;color:#5fc5ee}
.news .dots{left:9px;top:85px;width:168px;border-top:1px dotted #4b8ec7}
.btn-news{left:44px;top:101px;width:97px;height:20px;background:linear-gradient(#4cb8ef,#1b84d2);border:1px solid #0d5aa1;color:#0b2d5a;font-size:10px;text-align:center;line-height:18px}

/* why choose */
.why h2{left:29px;top:728px;font-family:"PT Sans Narrow",sans-serif;font-weight:400;font-size:17px;color:var(--heading)}
.why ul{left:33px;top:758px;width:340px;list-style:none}
.why li{font-size:8.2px;line-height:10px;color:#555;padding-left:12px;position:relative;margin-bottom:5.4px}
.why li::before{content:"";position:absolute;left:1px;top:2.5px;width:5px;height:5px;background:#777;transform:rotate(45deg)}

/* video */
.video{left:409px;top:731px;width:258px;height:215px;background:#000}
.video-frame{left:6px;top:6px;width:246px;height:178px;background:linear-gradient(135deg,#3a2a22,#7a5540 45%,#2a2c30 80%)}
.video-bar{left:6px;top:184px;width:246px;height:25px;background:#f3f3f3}
.cta{top:955px;height:31px;border-radius:5px;color:var(--white);font-size:13px;font-weight:700;text-align:center;line-height:30px}
.cta-price{left:409px;width:129px;background:linear-gradient(#7fd0f6,#2c95dc)}
.cta-quote{left:542px;width:125px;background:linear-gradient(#2b63bc,#06307a);border:1px solid #051f55}

/* accreditation + contact */
.sec-title{font-family:"PT Sans Narrow",sans-serif;font-weight:400;font-size:17px;color:var(--heading);display:flex;align-items:flex-end;gap:3px}
.sec-title i{display:block;border-bottom:1px dotted var(--heading);height:1px;margin-bottom:4px}
.accred{left:32px;top:1061px;width:423px;height:55px;background:#000;display:flex;align-items:center;gap:5px;padding:0 4px}
.badge{height:46px;background:#fff;flex:none}
.contact{left:490px;top:1058px;color:#333}
.contact p{font-size:11.5px;margin-bottom:6px}
.contact .phone{font-size:11.5px}
.contact .phone b{font-weight:400;font-size:15px;color:var(--heading);margin-left:6px}
.contact .mail b{font-weight:400;font-size:10px;color:var(--heading);margin-left:4px}

/* footer */
.site-footer{left:0;top:1136px;width:701px;height:64px;background:var(--blue);color:var(--white);text-align:center;font-size:7px;padding-top:20px;line-height:12px}
.site-footer a{color:var(--white);text-decoration:none;margin:0 3px}
</style>
</head>
<body>

<header class="site-header abs">
  <div class="brand abs"><span class="brand-mark"></span><span class="brand-name">Brightmark</span></div>
  <div class="call abs"><small>CALL US TODAY</small><strong>01632 960418</strong></div>
</header>

<nav class="main-nav abs">
  <a href="#">Home</a><a href="#">About Us</a><a href="#">Services</a><a href="#">Why PAT Test?</a><a href="#">Price Guarantee</a><a href="#">Latest News</a><a href="#">Contact Us</a>
</nav>

<section class="hero abs">
  <h1 class="abs">BRIGHTMARK<br>FOR ALL YOUR<br>ELECTRICAL AND SAFETY<br>REQUIREMENTS</h1>
  <div class="hero-art abs" role="img" aria-label="Fuse board, fire extinguisher, emergency exit sign, plug and fire alarm call point"></div>
</section>
<div class="hero-rule abs"></div>

<section class="services">
  <div class="service abs" style="left:30px;top:320px">
    <div class="thumb abs" role="img" aria-label="Electrical plug" style="background:linear-gradient(135deg,#f5f5f5,#2b2b2b 60%,#eee)"></div>
    <h3 class="abs">PAT Testing</h3><p class="abs">Lorem ipsum dolor sit amet, consectetur adipiscing elit. Nulla dolor odio.</p><span class="more abs">Read More ···· ›</span>
  </div>
  <div class="service abs" style="left:248px;top:320px">
    <div class="thumb abs" role="img" aria-label="Fuse board" style="background:linear-gradient(#e6e8ea,#b7bcc0)"></div>
    <h3 class="abs">FIXED Installion Testing</h3><p class="abs">Lorem ipsum dolor sit amet, consectetur adipiscing elit. Nulla dolor odio.</p><span class="more abs">Read More ···· ›</span>
  </div>
  <div class="service abs" style="left:30px;top:418px">
    <div class="thumb abs" role="img" aria-label="Fire alarm break glass point" style="background:linear-gradient(#d0241c,#1a1a1a 55%,#c21c16)"></div>
    <h3 class="abs">FIRE Alarm Maintenance</h3><p class="abs">Lorem ipsum dolor sit amet, consectetur adipiscing elit. Nulla dolor odio.</p><span class="more abs">Read More ···· ›</span>
  </div>
  <div class="service abs" style="left:248px;top:418px">
    <div class="thumb abs" role="img" aria-label="Fire extinguishers" style="background:linear-gradient(90deg,#8a8176,#c13a2f 50%,#d8d2c8)"></div>
    <h3 class="abs">FIRE Extinguisher Service</h3><p class="abs">Lorem ipsum dolor sit amet, consectetur adipiscing elit. Nulla dolor odio.</p><span class="more abs">Read More ···· ›</span>
  </div>
  <div class="service abs" style="left:30px;top:517px">
    <div class="thumb abs" role="img" aria-label="Emergency exit sign" style="background:linear-gradient(#f0f0f0,#2f9a55 40%,#eaeaea)"></div>
    <h3 class="abs">EMERGENCY Lighting</h3><p class="abs">Lorem ipsum dolor sit amet, consectetur adipiscing elit. Nulla dolor odio.</p><span class="more abs">Read More ···· ›</span>
  </div>
  <div class="service abs" style="left:248px;top:517px">
    <div class="thumb abs" role="img" aria-label="Electrician with test meter" style="background:linear-gradient(135deg,#e8e8e8,#3a5ea8 60%,#d9b89a)"></div>
    <h3 class="abs">ELECTRICAL Services</h3><p class="abs">Lorem ipsum dolor sit amet, consectetur adipiscing elit. Nulla dolor odio.</p><span class="more abs">Read More ···· ›</span>
  </div>
  <div class="service abs" style="left:30px;top:616px">
    <div class="thumb abs" role="img" aria-label="Thermal imaging camera" style="background:linear-gradient(135deg,#5a2a8a,#e0632a 50%,#2a1a5a)"></div>
    <h3 class="abs">THERMOGRAPHY</h3><p class="abs">Lorem ipsum dolor sit amet, consectetur adipiscing elit. Nulla dolor odio.</p><span class="more abs">Read More ···· ›</span>
  </div>
</section>

<aside>
  <div class="login abs">
    <h2 class="abs">LOGIN TO YOUR<br>BRIGHTMARK ACCOUNT</h2>
    <div class="field abs" style="top:59px">Type your userid</div>
    <div class="field abs" style="top:86px">••••••••••••••</div>
    <div class="btn-login abs">Login</div>
    <span class="forgot abs">Forgot your password? Click here</span>
    <span class="reg-q abs">Not Registered yet?</span>
    <span class="reg abs">REGISTER NOW! <span>ITS FREE</span></span>
  </div>
  <div class="follow abs"><span class="follow-text">follow us on<br>Chirpline</span><span class="follow-dot"></span></div>
  <div class="news abs">
    <h2 class="abs">LATEST NEWS</h2>
    <div class="divider abs"></div>
    <h4 class="abs">Lorem ipsum dolor sit amet</h4>
    <p class="abs">Lorem ipsum dolor sit amet, consectetur adipiscing elit. Nulla dolor odio expert di mario.</p>
    <div class="dots abs"></div>
    <div class="btn-news abs">Read More News</div>
  </div>
</aside>

<section class="why">
  <h2 class="abs">WHY CHOOSE BRIGHTMARK?</h2>
  <ul class="abs">
    <li>Full Range of Services Offered</li>
    <li>Established company with reputable client list</li>
    <li>Trustworthy company with fully employed staff</li>
    <li>Full liability insurance</li>
    <li>Experienced qualified engineers, all with full CRB checks</li>
    <li>Competitively priced with quotations On request</li>
    <li>No hidden charges</li>
    <li>Free small repairs</li>
    <li>All appliances tested, from 110v, 240v and 3 phase</li>
    <li>Free replacement of IEC leads, plugs and fuses</li>
    <li>bespoke scheduling software to ensure you are never out of date with your testing requirements</li>
    <li>Reports issued in your (or your insurance company's) preferred format.</li>
    <li>Out of hours service provided free of charge to minimise any disruption to business</li>
    <li>We guarantee to save you money on your safety testing</li>
    <li>Brightmark Approved for total peace of mind</li>
  </ul>
</section>

<div class="video abs">
  <div class="video-frame abs" role="img" aria-label="Video of an engineer testing equipment"></div>
  <div class="video-bar abs">
    <svg width="246" height="25" viewBox="0 0 246 25">
      <rect x="3" y="6" width="11" height="11" fill="#fff" stroke="#000"/><rect x="6" y="9" width="2" height="5"/><rect x="9" y="9" width="2" height="5"/>
      <rect x="17" y="6" width="11" height="11" fill="#fff" stroke="#000"/><rect x="20" y="9" width="5" height="5"/>
      <rect x="33" y="8" width="205" height="6" fill="#7fcc4a" stroke="#333"/>
      <rect x="109" y="5" width="4" height="12" fill="#fff" stroke="#333"/>
      <path d="M235 8 l4 3 -4 3z"/><rect x="241" y="8" width="1.5" height="6"/>
      <text x="128" y="23" font-size="6" font-family="Arimo,sans-serif" text-anchor="middle">00:00:24 / 00:01:05</text>
    </svg>
  </div>
</div>
<div class="cta cta-price abs">PRICE GUARANTEE</div>
<div class="cta cta-quote abs">FREE QUOTE</div>

<h2 class="sec-title abs" style="left:30px;top:1030px">OUR ACCREDIATATION <i style="width:120px"></i></h2>
<div class="accred abs">
  <div class="badge" style="width:68px;background:#000;border:1px solid #444"></div>
  <div class="badge" style="width:50px;border-radius:50%;background:#fff"></div>
  <div class="badge" style="width:92px;height:30px;background:#e4e4e4"></div>
  <div class="badge" style="width:125px"></div>
  <div class="badge" style="width:70px"></div>
</div>

<h2 class="sec-title abs" style="left:488px;top:1030px">CONTACT US <i style="width:108px"></i></h2>
<div class="contact abs">
  <p>For more information</p>
  <p class="phone">Call Us <b>01632 960418</b></p>
  <p class="mail">Email <b>info@brightmarkchecks.co.uk</b></p>
</div>

<footer class="site-footer abs">
  <a href="#">Home</a>| <a href="#">About Us</a>| <a href="#">Services</a>| <a href="#">Why PAT Test?</a>| <a href="#">Price Guarantee</a>| <a href="#">Latest News</a>| <a href="#">Contact Us</a>| <a href="#">Links</a><br>
  © 2012, All Rights Reserved, brightmarkchecks.co.uk
</footer>

</body>
</html>
```